Corporate id for sun shading company
Solvindu as
Simple
Rune Hovdal
Daglig leder
Lindhaugbakken 17 0482 OSLO
rune@solvindu.no
www.solvindu.no

```html
<!DOCTYPE html>
<html lang="no">
<head>
<meta charset="utf-8">
<title>Solvindu as – stationery</title>
<link rel="stylesheet" href="https://fonts.googleapis.com/css2?family=Lato:wght@400;700&family=Open+Sans:wght@400;600&display=swap">
<style>
  :root {
    --stage: #1e1e1e;
    --paper: #ffffff;
    --navy: #1b3a6b;
    --navy-deep: #15305a;
    --ink: #2b2b2b;
    --muted: #8a97ab;
    --rule: #44577a;
    --haze: #eef0f3;
  }
  * { box-sizing: border-box; margin: 0; padding: 0; }
  html, body { width: 1200px; height: 614px; overflow: hidden; background: var(--stage); }
  body { position: relative; font-family: "Lato", sans-serif; color: var(--ink); }

  .piece { position: absolute; background: var(--paper); overflow: hidden; }

  .brand { position: absolute; display: flex; flex-direction: column; align-items: center; gap: 6px; }
  .brand-dot { width: 24px; height: 24px; border-radius: 50%; background: var(--navy); }
  .wordmark { font-family: "Open Sans", sans-serif; font-weight: 400; color: var(--navy); letter-spacing: .06em; white-space: nowrap; line-height: 1; }
  .brand.on-navy .brand-dot { background: #fff; }
  .brand.on-navy .wordmark { color: #fff; }

  .backdrop { position: absolute; }

  .rule { position: absolute; height: 1px; background: var(--rule); }
  .rule::before { content: ""; position: absolute; left: 0; top: -1px; height: 2px; width: 28%; background: var(--navy); }

  .contact { position: absolute; font-family: "Open Sans", sans-serif; color: var(--ink); }
  .contact li { list-style: none; display: flex; align-items: center; gap: 3px; }
  .contact.right li { justify-content: flex-end; }
  .contact svg { fill: var(--navy); flex: none; }
  .contact .web { color: var(--navy); }

  .signer-name { font-weight: 700; color: var(--navy); }
  .signer-role { color: var(--muted); }

  /* business card front */
  .card-front { left: 25px; top: 288px; width: 241px; height: 135px; }
  .card-front .backdrop { left: 0; top: 0; width: 104px; height: 135px;
    background: linear-gradient(90deg, var(--haze) 0%, rgba(238,240,243,.6) 70%, rgba(238,240,243,0) 100%);
    border-radius: 0 0 60px 0; }
  .card-front .brand { right: 12px; top: 13px; gap: 5px; }
  .card-front .brand-dot { width: 22px; height: 22px; }
  .card-front .wordmark { font-size: 12.5px; }
  .card-front .signer { position: absolute; left: 12px; top: 70px; line-height: 1.05; }
  .card-front .signer-name { font-size: 8.5px; }
  .card-front .signer-role { font-size: 5.5px; }
  .card-front .rule { left: 12px; right: 11px; top: 92px; }
  .card-front .contact { font-size: 5.5px; line-height: 9px; top: 98px; }
  .card-front .contact.left { left: 12px; }
  .card-front .contact.right { right: 11px; }

  /* business card back */
  .card-back { left: 25px; top: 449px; width: 241px; height: 135px; background: var(--navy); }
  .pattern-fill { position: absolute; inset: 0; background: radial-gradient(circle at 50% 50%, #24467c 0%, var(--navy) 55%, var(--navy-deep) 100%); }
  .card-back .brand { left: 50%; top: 50%; transform: translate(-50%, -50%); }
  .card-back .wordmark { font-size: 12.5px; }

  /* letterhead */
  .letter { left: 289px; top: 25px; width: 396px; height: 558px; }
  .letter .backdrop { left: 0; top: 0; width: 340px; height: 490px;
    background: linear-gradient(180deg, rgba(238,240,243,.9) 0%, rgba(238,240,243,.7) 55%, rgba(238,240,243,0) 100%);
    border-radius: 0 0 240px 0; }
  .letter .brand { right: 26px; top: 36px; }
  .letter .brand-dot { width: 26px; height: 26px; }
  .letter .wordmark { font-size: 14px; }
  .letter .body { position: absolute; left: 25px; top: 176px; width: 348px; font-size: 6.2px; line-height: 8.6px; }
  .letter .body p { margin-bottom: 8.6px; }
  .letter .greeting { margin-bottom: 17px !important; }
  .letter .signer { position: absolute; left: 25px; top: 361px; line-height: 1.1; }
  .letter .signer-name { font-size: 8.5px; }
  .letter .signer-role { font-size: 5.8px; }
  .letter .rule { left: 25px; right: 26px; top: 500px; }
  .letter .contact { top: 507px; font-size: 6px; line-height: 9.8px; }
  .letter .contact.left { left: 25px; }
  .letter .contact.right { right: 26px; }

  /* envelope back with flap */
  .envelope-back { left: 704px; top: 150px; width: 466px; height: 208px; }
  .envelope-back svg.flap { position: absolute; left: 0; top: 0; }
  .envelope-back .brand { left: 50%; top: 14px; transform: translateX(-50%); gap: 5px; }
  .envelope-back .brand-dot { width: 22px; height: 22px; }
  .envelope-back .wordmark { font-size: 11px; }

  /* envelope front */
  .envelope-front { left: 704px; top: 376px; width: 466px; height: 208px; }
  .envelope-front .backdrop { right: 0; top: 0; width: 145px; height: 208px;
    background: linear-gradient(270deg, var(--haze) 0%, rgba(238,240,243,.7) 60%, rgba(238,240,243,0) 100%);
    border-radius: 0 0 0 90px; }
  .envelope-front .brand { left: 18px; top: 16px; }
  .envelope-front .brand-dot { width: 26px; height: 26px; }
  .envelope-front .wordmark { font-size: 15px; }
  .envelope-front .rule { left: 18px; right: 25px; top: 177px; }
  .envelope-front .contact { top: 183px; font-size: 6.2px; }
  .envelope-front .contact.left { left: 18px; }
  .envelope-front .contact.right { right: 25px; }
</style>
</head>
<body>

  <!-- Business card, front -->
  <section class="piece card-front">
    <div class="backdrop" role="img" aria-label="Faint striped brand decoration"></div>
    <div class="brand"><span class="brand-dot"></span><div class="wordmark">SOLVINDU</div></div>
    <div class="signer">
      <div class="signer-name">Rune Hovdal</div>
      <div class="signer-role">Daglig leder</div>
    </div>
    <div class="rule"></div>
    <ul class="contact left">
      <li><svg width="6" height="5" viewBox="0 0 12 10"><path d="M1 3c0-2 10-2 10 0v1H8V3H4v1H1zM3 5h6l2 4H1z"/></svg>40012345</li>
      <li><svg width="6" height="5" viewBox="0 0 12 10"><path d="M1 3c0-2 10-2 10 0v1H8V3H4v1H1zM3 5h6l2 4H1z"/></svg>92837465</li>
      <li><svg width="6" height="4" viewBox="0 0 12 8"><path d="M0 0h12v8H0zM1 1l5 4 5-4" stroke="#fff" stroke-width="1"/></svg>rune@solvindu.no</li>
    </ul>
    <ul class="contact right">
      <li>Lindhaugbakken 17</li>
      <li>0482 OSLO</li>
      <li class="web">solvindu.no</li>
    </ul>
  </section>

  <!-- Business card, back -->
  <section class="piece card-back">
    <div class="pattern-fill" role="img" aria-label="Navy tiled brand pattern"></div>
    <div class="brand on-navy"><span class="brand-dot"></span><div class="wordmark">SOLVINDU</div></div>
  </section>

  <!-- Letterhead -->
  <section class="piece letter">
    <div class="backdrop" role="img" aria-label="Faint striped brand decoration"></div>
    <div class="brand"><span class="brand-dot"></span><div class="wordmark">SOLVINDU</div></div>
    <div class="body">
      <p class="greeting">Dear Mr. Larsen,</p>
      <p>Lorem ipsum dolor sit amet, consectetur adipiscing elit. Donec orci purus, luctus vitae dignissim eu, iaculis sed purus. Vivamus faucibus, ipsum nec aliquet viverra, leo mauris condimentum ligula, sit amet sagittis enim ligula quis arcu. Nam egestas tortor id nisi porttitor mattis. In tortor ante, ultricies in suscipit a, tempus non massa. Vivamus et auctor mi.</p>
      <p>Fusce vel massa nulla. Phasellus nec eros mauris, et scelerisque orci. Donec malesuada orci vitae nulla accumsan porta a id massa. Quisque accumsan iaculis magna sit amet fringilla. Maecenas consequat, magna eget tincidunt semper, odio nibh rutrum mi, id feugiat ante nisi eu risus. Vestibulum nunc orci, rhoncus a placerat in, ultricies in mi. Cras mattis varius eros, vel fringilla nisi suscipit eget.</p>
      <p>Quisque scelerisque sagittis nulla at porttitor. Mauris a justo et tellus interdum tristique. Sed id augue vitae urna euismod commodo aliquet a quam. Pellentesque arcu velit, cursus et malesuada ut, consequat et diam. Nullam erat sem, rhoncus id ullamcorper vitae, rhoncus et arcu. In ultricies ultricies nulla, ut rutrum nisi iaculis at. Donec eu magna a metus ornare faucibus.</p>
      <p>Fusce aliquet faucibus ultricies. Morbi semper, est id tincidunt gravida, sem arcu adipiscing lacus, ac bibendum nulla leo eu purus. Quisque nec diam sed risus consectetur a ccumsan quis quis nibh. Vestibulum id purus lorem.</p>
    </div>
    <div class="signer">
      <div class="signer-name">Rune Hovdal</div>
      <div class="signer-role">Daglig leder</div>
    </div>
    <div class="rule"></div>
    <ul class="contact left">
      <li><svg width="7" height="6" viewBox="0 0 12 10"><path d="M1 3c0-2 10-2 10 0v1H8V3H4v1H1zM3 5h6l2 4H1z"/></svg>40012345</li>
      <li><svg width="7" height="6" viewBox="0 0 12 10"><path d="M1 3c0-2 10-2 10 0v1H8V3H4v1H1zM3 5h6l2 4H1z"/></svg>92837465</li>
      <li><svg width="7" height="5" viewBox="0 0 12 8"><path d="M0 0h12v8H0zM1 1l5 4 5-4" stroke="#fff" stroke-width="1"/></svg>rune@solvindu.no</li>
    </ul>
    <ul class="contact right">
      <li>Lindhaugbakken 17</li>
      <li>0482 OSLO</li>
      <li class="web">www.solvindu.no</li>
    </ul>
  </section>

  <!-- Envelope, back with flap -->
  <section class="piece envelope-back">
    <svg class="flap" width="466" height="80" viewBox="0 0 466 80" role="img" aria-label="Navy envelope flap with tiled brand pattern">
      <defs>
        <radialGradient id="flapTone" cx="50%" cy="40%" r="60%">
          <stop offset="0" stop-color="#24467c"/>
          <stop offset="1" stop-color="#17335f"/>
        </radialGradient>
      </defs>
      <path d="M0 0H466L458 44Q452 77 420 77H46Q14 77 8 44Z" fill="url(#flapTone)"/>
    </svg>
    <div class="brand on-navy"><span class="brand-dot"></span><div class="wordmark">SOLVINDU</div></div>
  </section>

  <!-- Envelope, front -->
  <section class="piece envelope-front">
    <div class="backdrop" role="img" aria-label="Faint striped brand decoration"></div>
    <div class="brand"><span class="brand-dot"></span><div class="wordmark">SOLVINDU</div></div>
    <div class="rule"></div>
    <div class="contact left">Lindhaugbakken 17, 0482 OSLO</div>
    <div class="contact right"><span class="web">www.solvindu.no</span></div>
  </section>

</body>
</html>
```